KRT Civils*

we are a construction company specialising in Housing, Water Infrastructure and Roadworks
This is the description I would like to be added to the Flyer. I have
also attached a Picture
Krt Civils is a Construction Company specializing in Housing, Roadworks
and Water infrastructure. Krt has established itself firmly in the
Construction industry with branches all through Southern Africa as well
as into Africa.
Krt is committed to giving its Clients efficient and Professional
service at all times, We pride ourselves on our ability to meet
deadlines and exceed expectations. Our aim is to establish Successful
Long lasting relationships with our Client base
Colors
Designer to choose only greyscale colors for use in the design.
Look and feel

```html
<!DOCTYPE html>
<html lang="en">
<head>
<meta charset="utf-8">
<title>KRT Civils Flyer</title>
<link href="https://fonts.googleapis.com/css2?family=Open+Sans:wght@300;400;600;800&display=swap" rel="stylesheet">
<style>
  :root {
    --page-bg: #e4e4e4;
    --paper: #ffffff;
    --ink: #1a1a1a;
    --text: #2b2b2b;
    --brand-red: #c1272d;
    --band-black: #111111;
    --photo-sky: #b9c6cf;
    --photo-hills: #6f8296;
    --photo-roofs: #b98a6e;
    --photo-grass: #8a8a5a;
  }
  * { box-sizing: border-box; margin: 0; padding: 0; }
  html, body {
    width: 1200px; height: 880px; overflow: hidden;
    background: var(--page-bg);
    font-family: "Open Sans", Arial, sans-serif;
  }
  .flyer {
    position: absolute; left: 300px; top: 16px;
    width: 600px; height: 848px;
    background: var(--paper);
    box-shadow: 0 6px 20px rgba(0,0,0,0.18);
    overflow: hidden;
  }
  .brand { position: absolute; left: 44px; top: 48px; }
  .brand-row { display: flex; align-items: center; gap: 14px; }
  .brand-mark { width: 26px; height: 26px; background: var(--ink); }
  .brand-name {
    font-weight: 800; font-size: 54px; letter-spacing: 2px;
    color: var(--ink); line-height: 1;
  }
  .services {
    margin-top: 16px; font-size: 15px; font-weight: 400;
    color: var(--brand-red); letter-spacing: 0.5px; text-transform: uppercase;
  }
  .services .sep { color: var(--ink); margin: 0 8px; }
  .hero-photo {
    position: absolute; left: 0; top: 170px; width: 600px; height: 330px;
    background: linear-gradient(180deg, var(--photo-sky) 0%, var(--photo-hills) 28%, var(--photo-roofs) 52%, #c9b79a 70%, var(--photo-grass) 100%);
  }
  .bands { position: absolute; left: 0; top: 400px; width: 600px; height: 150px; }
  .title {
    position: absolute; left: 40px; top: 454px;
    font-weight: 300; font-size: 50px; color: #fff; line-height: 1;
  }
  .about {
    position: absolute; left: 44px; top: 568px; width: 350px;
    font-size: 14.5px; line-height: 1.45; color: var(--text);
  }
  .about p + p { margin-top: 20px; }
  .service-icons {
    position: absolute; left: 452px; top: 430px;
    display: flex; flex-direction: column; gap: 28px;
  }
  .service-icons svg { width: 92px; height: 92px; display: block; }
</style>
</head>
<body>
  <main class="flyer">
    <header class="brand">
      <div class="brand-row">
        <span class="brand-mark"></span>
        <span class="brand-name">KRT CIVILS</span>
      </div>
      <p class="services">Housing<span class="sep">|</span>Water Infrastructure<span class="sep">|</span>Roadworks</p>
    </header>

    <div class="hero-photo" role="img" aria-label="Photo of a new housing development with rows of roofs, hills and sky behind"></div>

    <svg class="bands" viewBox="0 0 600 150" aria-hidden="true">
      <polygon points="340,10 600,10 600,90 310,90" fill="var(--band-black)"/>
      <polygon points="0,40 370,40 330,150 0,150" fill="var(--brand-red)"/>
    </svg>
    <h1 class="title">Krt Civils</h1>

    <section class="about">
      <p>Krt Civils is a Construction Company specializing in Housing, Roadworks and Water infrastructure. Krt has established itself firmly in the Construction industry with branches all through Southern Africa as well as into Africa.</p>
      <p>Krt is committed to giving its Clients efficient and Professional service at all times, We pride ourselves on our ability to meet deadlines and exceed expectations. Our aim is to establish Successful Long lasting relationships with our Client base</p>
    </section>

    <div class="service-icons">
      <svg viewBox="0 0 92 92" role="img" aria-label="Housing">
        <circle cx="46" cy="46" r="44" fill="var(--brand-red)" stroke="#fff" stroke-width="3"/>
        <polygon points="46,20 72,42 66,42 66,68 26,68 26,42 20,42" fill="#fff"/>
        <rect x="40" y="48" width="12" height="20" fill="var(--brand-red)"/>
      </svg>
      <svg viewBox="0 0 92 92" role="img" aria-label="Water infrastructure">
        <circle cx="46" cy="46" r="44" fill="var(--brand-red)"/>
        <path d="M46 18 C38 34 30 44 30 54 a16 16 0 0 0 32 0 C62 44 54 34 46 18 Z" fill="#fff"/>
      </svg>
      <svg viewBox="0 0 92 92" role="img" aria-label="Roadworks">
        <circle cx="46" cy="46" r="44" fill="var(--brand-red)"/>
        <polygon points="38,20 54,20 70,72 22,72" fill="#fff"/>
        <rect x="44" y="26" width="4" height="10" fill="var(--brand-red)"/>
        <rect x="44" y="42" width="4" height="12" fill="var(--brand-red)"/>
        <rect x="44" y="60" width="4" height="12" fill="var(--brand-red)"/>
      </svg>
    </div>
  </main>
</body>
</html>
```